Business Card Design for boarding house accomodation business

I need a business card design for my Sydney based boarding house business accomodation. providing rooms for rent in Sydney Australia with shard bathroom and kitchen.
The front of card, are my details with details of head office and the rear of card to have details of locations providing rooms for rent.

Industry/Entity Type

Business

Contact Information for Business Card

Front of card details:
HOLLINBROOK MANAGEMENT PTY LTD t/a
CALLOWAY'S GUEST HOUSE
ABN:52930718264
Daniel Vukasinov
48 Pembury st
Newtown 2042
Mobile:0412876390
Email:daniel@callowaysguesthouse-example.com.au

Back of Card:
Locations:
-48 Pembury st
Newtown 2042

-392 Carvel st
Erskineville 2043

-87 Whitlam st
Bondi 2026

-264 Ashcombe rd
Marrickville 2043

```html
<!DOCTYPE html>
<html lang="en">
<head>
<meta charset="utf-8">
<title>Calloway's Guest House – Business Card</title>
<link rel="stylesheet" href="https://fonts.googleapis.com/css2?family=Arimo:wght@400;700&family=Tinos:wght@400;700&display=swap">
<style>
  :root {
    --bg: #e9e6e1;
    --paper: #f7f7f7;
    --ink: #1c1c1c;
    --ink-soft: #2a2a2a;
    --navy: #1e2f82;
    --navy-deep: #16246a;
    --band-black: #111111;
    --white: #ffffff;
    --rule: #c9cde0;
  }
  * { box-sizing: border-box; margin: 0; padding: 0; }
  html, body { width: 1200px; height: 902px; overflow: hidden; background: var(--bg); }
  .canvas {
    width: 1200px; height: 902px;
    display: flex; flex-direction: column; align-items: center; justify-content: center; gap: 40px;
  }
  .card {
    position: relative; width: 700px; height: 400px; background: var(--paper);
    box-shadow: 0 6px 18px rgba(0,0,0,.18); overflow: hidden;
  }

  /* Front */
  .front__identity { position: absolute; top: 0; left: 0; right: 0; height: 222px; text-align: center; padding-top: 52px; }
  .company { font-family: "Tinos", serif; font-weight: 700; font-size: 40px; color: var(--ink); letter-spacing: .3px; }
  .trading-name { font-family: "Arimo", sans-serif; font-weight: 700; font-size: 27px; color: var(--ink-soft); margin-top: 4px; }
  .abn { font-family: "Arimo", sans-serif; font-size: 21px; color: var(--ink-soft); margin-top: 18px; }
  .band-black { position: absolute; left: 0; right: 0; background: var(--band-black); }
  .band-navy { position: absolute; left: 0; right: 0; bottom: 0; background: linear-gradient(180deg, var(--navy) 0%, var(--navy-deep) 100%); }
  .front .band-black { top: 222px; height: 16px; }
  .front .band-navy { top: 238px; }
  .holder { position: absolute; left: 36px; bottom: 42px; font-family: "Tinos", serif; font-weight: 700; font-size: 31px; color: var(--white); }
  .divider { position: absolute; left: 318px; top: 22px; bottom: 22px; width: 1.5px; background: var(--rule); }
  .contacts { position: absolute; left: 336px; top: 34px; list-style: none; }
  .contacts li { display: flex; align-items: center; gap: 10px; font-family: "Arimo", sans-serif; font-size: 15px; color: var(--white); height: 32px; }
  .contacts svg { width: 20px; height: 20px; flex: none; }

  /* Back */
  .locations-title { position: absolute; left: 40px; top: 120px; font-family: "Tinos", serif; font-weight: 700; font-size: 40px; color: var(--navy); }
  .locations { position: absolute; left: 238px; top: 58px; list-style: none; }
  .locations li { display: flex; align-items: center; gap: 16px; font-family: "Arimo", sans-serif; font-size: 21px; color: var(--ink-soft); height: 50px; }
  .locations svg { width: 22px; height: 22px; flex: none; }
  .back .band-black { top: 318px; height: 14px; }
  .back .band-navy { top: 332px; }
</style>
</head>
<body>
<main class="canvas">

  <section class="card front" aria-label="Card front">
    <div class="front__identity">
      <p class="company">Hollinbrook Management Pty Ltd</p>
      <p class="trading-name">Calloway's Guest House</p>
      <p class="abn">ABN:52930718264</p>
    </div>
    <div class="band-black"></div>
    <div class="band-navy">
      <p class="holder">Daniel Vukasinov</p>
      <div class="divider"></div>
      <ul class="contacts">
        <li>
          <svg viewBox="0 0 20 20" aria-hidden="true"><rect width="20" height="20" rx="2" fill="#fff"/><path d="M5 7c0-1 1-2 2-2h6c1 0 2 1 2 2v1h-3V7H8v1H5z M6 9h8l1 6H5z" fill="#1e2f82"/><circle cx="10" cy="12" r="1.6" fill="#fff"/></svg>
          0412876390
        </li>
        <li>
          <svg viewBox="0 0 20 20" aria-hidden="true"><rect width="20" height="20" rx="2" fill="#fff"/><rect x="4" y="6" width="12" height="8" fill="#1e2f82"/><path d="M4 6l6 5 6-5" stroke="#fff" stroke-width="1.2" fill="none"/></svg>
          daniel@callowaysguesthouse-example.com.au
        </li>
        <li>
          <svg viewBox="0 0 20 20" aria-hidden="true"><rect width="20" height="20" rx="2" fill="#fff"/><path d="M10 4l6 6h-2v6H6v-6H4z" fill="#1e2f82"/><rect x="9" y="12" width="2" height="4" fill="#fff"/></svg>
          48 Pembury st Newtown 2042
        </li>
      </ul>
    </div>
  </section>

  <section class="card back" aria-label="Card back">
    <p class="locations-title">Locations:</p>
    <ul class="locations">
      <li><svg viewBox="0 0 22 22" aria-hidden="true"><circle cx="11" cy="11" r="7" fill="none" stroke="#1e2f82" stroke-width="1.4"/><circle cx="11" cy="11" r="3" fill="#1e2f82"/><path d="M11 1v5M11 16v5M1 11h5M16 11h5" stroke="#1e2f82" stroke-width="1.4"/></svg>48 Pembury st, Newtown 2042</li>
      <li><svg viewBox="0 0 22 22" aria-hidden="true"><circle cx="11" cy="11" r="7" fill="none" stroke="#1e2f82" stroke-width="1.4"/><circle cx="11" cy="11" r="3" fill="#1e2f82"/><path d="M11 1v5M11 16v5M1 11h5M16 11h5" stroke="#1e2f82" stroke-width="1.4"/></svg>392 Carvel st, Erskineville 2043</li>
      <li><svg viewBox="0 0 22 22" aria-hidden="true"><circle cx="11" cy="11" r="7" fill="none" stroke="#1e2f82" stroke-width="1.4"/><circle cx="11" cy="11" r="3" fill="#1e2f82"/><path d="M11 1v5M11 16v5M1 11h5M16 11h5" stroke="#1e2f82" stroke-width="1.4"/></svg>87 Whitlam st, Bondi 2026</li>
      <li><svg viewBox="0 0 22 22" aria-hidden="true"><circle cx="11" cy="11" r="7" fill="none" stroke="#1e2f82" stroke-width="1.4"/><circle cx="11" cy="11" r="3" fill="#1e2f82"/><path d="M11 1v5M11 16v5M1 11h5M16 11h5" stroke="#1e2f82" stroke-width="1.4"/></svg>264 Ashcombe rd, Marrickville 2043</li>
    </ul>
    <div class="band-black"></div>
    <div class="band-navy"></div>
  </section>

</main>
</body>
</html>
```